Online Psychology Practice needs business cards.

Online Psychology service needs business cards. Have own logo- please see uploaded. I have other file formats if you need (not sure one needed?)

Details for Business Card:
Fiona Kettlewood
Clinical Psychologist BPsych, BPsych (Hons), MPsych (Clin), MAPS
T: 0457260714 | F: 08 71526804
E: hello@harbourlightmindcarestudio.com.au
W: harbourlightmindcarestudio.com.au

Industry/Entity Type

Health

Contact Information for Business Card

Logo plus details above (couldn't write in this section)

```html
<!DOCTYPE html>
<html lang="en">
<head>
<meta charset="utf-8">
<title>Harbourlight Mindcare Studio – Business Cards</title>
<link rel="stylesheet" href="https://fonts.googleapis.com/css2?family=Cinzel:wght@500&family=Montserrat:wght@400;500&display=swap">
<style>
  :root {
    --stage: #2b2b2b;
    --card-dark: #232323;
    --card-black: #151515;
    --pattern-tone: #1e1e1e;
    --paper: #ffffff;
    --brand-blue: #1f6fae;
    --brand-teal: #1097b3;
    --text-light: #f2f2f2;
  }
  * { margin: 0; padding: 0; box-sizing: border-box; }
  html, body { width: 1200px; height: 874px; overflow: hidden; }
  body {
    background: var(--stage);
    display: flex;
    flex-direction: column;
    align-items: center;
    justify-content: center;
    gap: 40px;
  }
  .card {
    position: relative;
    width: 640px;
    height: 366px;
    overflow: hidden;
    box-shadow: 0 12px 30px rgba(0,0,0,0.45);
  }

  /* Back */
  .card-back { background: var(--card-black); }
  .back-pattern {
    position: absolute; inset: 0;
    background: radial-gradient(circle at 40% 40%, var(--pattern-tone), var(--card-black) 75%);
  }
  .back-brand {
    position: absolute;
    right: 34px; bottom: 32px;
    display: flex; align-items: center; gap: 8px;
    font-family: "Cinzel", serif;
    font-weight: 500;
    font-size: 13px;
    letter-spacing: 1px;
    color: var(--brand-teal);
  }
  .brand-dot {
    width: 10px; height: 10px; border-radius: 50%;
    background: var(--brand-teal);
  }

  /* Front */
  .card-front { background: var(--paper); }
  .front-figure {
    position: absolute;
    left: 270px; top: 0;
    width: 370px; height: 366px;
    background: radial-gradient(ellipse at 45% 55%, rgba(16,151,179,0.55), rgba(16,151,179,0.12) 55%, var(--paper) 80%);
  }
  .front-panel { position: absolute; inset: 0; }
  .front-info {
    position: absolute;
    left: 28px; top: 40px;
    width: 262px;
  }
  .front-brand {
    font-family: "Cinzel", serif;
    font-weight: 500;
    font-size: 21px;
    line-height: 1.15;
    color: var(--brand-blue);
    text-align: center;
    width: 250px;
    letter-spacing: 1px;
  }
  .person-name {
    margin-top: 34px;
    font-family: "Cinzel", serif;
    font-weight: 500;
    font-size: 21px;
    color: var(--brand-blue);
    letter-spacing: 0.5px;
    white-space: nowrap;
  }
  .person-role {
    margin-top: 4px;
    font-family: "Montserrat", sans-serif;
    font-size: 13px;
    color: var(--brand-blue);
  }
  .person-credentials {
    margin-top: 2px;
    font-family: "Montserrat", sans-serif;
    font-size: 9px;
    color: var(--brand-blue);
  }
  .contact-list {
    list-style: none;
    margin-top: 20px;
    font-family: "Montserrat", sans-serif;
    font-size: 10.5px;
    color: var(--text-light);
  }
  .contact-list li {
    display: flex; align-items: center; gap: 7px;
    margin-bottom: 7px;
    white-space: nowrap;
  }
  .contact-list .phone-line { font-size: 13px; }
  .icon { width: 11px; height: 11px; flex: none; fill: var(--brand-teal); }
  .fax-gap { margin-left: 8px; }
</style>
</head>
<body>

  <section class="card card-back">
    <div class="back-pattern" role="img" aria-label="Embossed repeating floral pattern in black"></div>
    <div class="back-brand"><span class="brand-dot"></span>Harbourlight Mindcare Studio</div>
  </section>

  <section class="card card-front">
    <div class="front-figure" role="img" aria-label="Large teal figure with raised arms on white"></div>
    <svg class="front-panel" width="640" height="366" viewBox="0 0 640 366">
      <path d="M0 0 H292 Q322 230 262 366 H0 Z" fill="var(--card-dark)"/>
    </svg>
    <div class="front-info">
      <div class="front-brand">Harbourlight<br>Mindcare Studio</div>
      <div class="person-name">FIONA KETTLEWOOD</div>
      <div class="person-role">Clinical Psychologist BPsych,</div>
      <div class="person-credentials">BPsych (Hons), MPsych (Clin), MAPS</div>
      <ul class="contact-list">
        <li class="phone-line">
          <svg class="icon" viewBox="0 0 24 24"><path d="M6.6 10.8a15 15 0 0 0 6.6 6.6l2.2-2.2a1 1 0 0 1 1-.25 11 11 0 0 0 3.6.6 1 1 0 0 1 1 1V20a1 1 0 0 1-1 1A17 17 0 0 1 3 4a1 1 0 0 1 1-1h3.5a1 1 0 0 1 1 1 11 11 0 0 0 .6 3.6 1 1 0 0 1-.25 1z"/></svg>
          0457260714
          <svg class="icon fax-gap" viewBox="0 0 24 24"><path d="M6 3h10v5H6zM3 9h18v9h-3v3H6v-3H3zm5 6v4h8v-4z"/></svg>
          08 71526804
        </li>
        <li>
          <svg class="icon" viewBox="0 0 24 24"><path d="M2 5h20v14H2zm2 2v.5l8 5 8-5V7z"/></svg>
          hello@harbourlightmindcarestudio.com.au
        </li>
        <li>
          <svg class="icon" viewBox="0 0 24 24"><circle cx="12" cy="12" r="10"/></svg>
          harbourlightmindcarestudio.com.au
        </li>
      </ul>
    </div>
  </section>

</body>
</html>
```